Business Card for: Keelwright Financial Advisory Services Inc.

provide strategic financial advisory services to companies in the areas of corporate finance, mergers and acquisitions, executive coaching and strategic planning

Target Market(s)

Companies, banks, accountants, lawyers

Industry/Entity Type

High end business consulting in corporate finance, mergers and acquisitions, consulting

Contact Information for Business Card

Name of company, Name: xxxxxx xxxxxx , CEO, - phone number: 1-xxx-xxx-xxxx, - email address,

Requirements
Must have
• Must be professional and simple.
Nice to have
• simple, straight graphics, must give the impression that we are trustworthy, professional, competent
Should not have
• loud colors, loud design features

```html
<!DOCTYPE html>
<html lang="en">
<head>
<meta charset="utf-8">
<title>Keelwright Financial Advisory Services Inc. – Business Card</title>
<link href="https://fonts.googleapis.com/css2?family=Montserrat:wght@300;400;700&display=swap" rel="stylesheet">
<style>
  :root {
    --backdrop: #555657;
    --brand-blue: #1a4e9e;
    --paper: #f7f7f5;
    --text-dark: #3a3a3a;
    --white: #ffffff;
  }
  * { margin: 0; padding: 0; box-sizing: border-box; }
  html, body {
    width: 1200px; height: 801px; overflow: hidden;
    background: var(--backdrop);
    font-family: "Montserrat", sans-serif;
  }
  .sheet {
    position: relative; width: 1200px; height: 801px;
  }
  .card {
    position: absolute; top: 252px;
    width: 525px; height: 300px;
    overflow: hidden;
    box-shadow: 0 10px 30px rgba(0,0,0,0.35);
  }
  /* Front */
  .card-front { left: 50px; background: var(--brand-blue); color: var(--white); }
  .edge-bar {
    position: absolute; width: 18px; height: 52px;
  }
  .card-front .edge-bar { left: 300px; background: var(--white); }
  .edge-bar.top { top: 0; }
  .edge-bar.bottom { bottom: 0; }
  .wordmark {
    position: absolute; left: 78px; top: 112px;
  }
  .wordmark-name {
    font-weight: 300; font-size: 54px; letter-spacing: -0.5px; line-height: 1;
  }
  .wordmark-tagline {
    font-weight: 400; font-size: 15.5px; letter-spacing: 0.3px; margin-top: 4px; padding-left: 2px;
  }
  /* Back */
  .card-back { left: 625px; background: var(--paper); color: var(--brand-blue); }
  .card-back .edge-bar {
    right: 0; width: 52px; height: 18px; background: var(--brand-blue);
  }
  .card-back .edge-bar.top { top: 62px; }
  .card-back .edge-bar.bottom { top: auto; bottom: 62px; }
  .contact-list {
    position: absolute; left: 34px; top: 40px; list-style: none;
  }
  .contact-item {
    display: flex; align-items: center; gap: 16px;
    font-size: 11px; color: var(--text-dark); margin-bottom: 16px;
  }
  .contact-icon { width: 16px; height: 16px; flex: none; }
  .identity {
    position: absolute; right: 78px; top: 132px; text-align: right;
  }
  .identity-company { font-weight: 300; font-size: 26px; line-height: 1; }
  .identity-company-tagline { font-size: 7.5px; letter-spacing: 0.2px; margin-top: 2px; }
  .person-name { font-weight: 700; font-size: 34px; margin-top: 14px; line-height: 1.1; }
  .person-rule {
    width: 110px; height: 1.5px; background: var(--brand-blue); margin: 6px 0 4px auto;
  }
  .person-title { font-weight: 300; font-size: 15px; letter-spacing: 1px; padding-right: 30px; }
</style>
</head>
<body>
<main class="sheet">

  <section class="card card-front" aria-label="Business card front">
    <span class="edge-bar top"></span>
    <span class="edge-bar bottom"></span>
    <div class="wordmark">
      <div class="wordmark-name">Keelwright</div>
      <div class="wordmark-tagline">Financial Advisory Services Inc.</div>
    </div>
  </section>

  <section class="card card-back" aria-label="Business card back">
    <span class="edge-bar top"></span>
    <span class="edge-bar bottom"></span>

    <ul class="contact-list">
      <li class="contact-item">
        <svg class="contact-icon" viewBox="0 0 16 16" aria-hidden="true">
          <path d="M4.5 1.5 C3 2.2 2.5 4 3 6 C3.8 9.5 6.5 12.6 9.8 14 C11.6 14.7 13 14 13.8 12.8 L11.5 10.6 C11 11 10.3 11.3 9.7 11 C8 10 6.3 8 5.7 6.3 C5.5 5.7 5.8 5 6.3 4.6 Z" fill="var(--brand-blue)"/>
        </svg>
        <span>+1 (416) 555-0192</span>
      </li>
      <li class="contact-item">
        <svg class="contact-icon" viewBox="0 0 16 16" aria-hidden="true">
          <rect x="1" y="3.5" width="14" height="9" fill="var(--brand-blue)"/>
          <path d="M1.5 4 L8 9 L14.5 4 M1.5 12 L6 8 M14.5 12 L10 8" stroke="var(--paper)" stroke-width="1" fill="none"/>
        </svg>
        <span>daniel.brooks@keelwrightadvisory.com</span>
      </li>
    </ul>

    <div class="identity">
      <div class="identity-company">Keelwright</div>
      <div class="identity-company-tagline">Financial Advisory Services Inc.</div>
      <div class="person-name">Daniel Brooks</div>
      <div class="person-rule"></div>
      <div class="person-title">CEO</div>
    </div>
  </section>

</main>
</body>
</html>
```